Halvard Atelier Business cards

Design our business cards and eventually a logo. The company is based in Paris, its activity is the retailing via internet of luxury home furniture (like Vambrelli, Bercusa, tarvoni...) Our clients are international andwith a high sense of aesthetics. The design shall communicate wealth and trust with a high quality and aesthetic sense, pure lines Company Name is Halvard AtelierExplanation of the name: usually people who wants to buy furniture usually go in a showroom. Today they go in showroom to test the furniture and they search for the price on internet, which is a "Halvard atelier".We will not be a e-commerce site. Our site will be (another project) a presentation site which purpose is to reach qualified prospects. Then everything will be handled by phone, meeting etc.The business card must be professional as we will negotiate with many luxury brands, opportunity to represent them on our site, prices etc.As far as the color are concerned mostly black and whithe or grey. The font of the Halvard Atelier name shall have some impact.

Target Market(s)

High-end furniture and buyers of luxury goods, international customers, mostly women who handle such projects.
We also deal with professional buyers (hotels as an example) and luxury brands

Contact Information for Business Card

standard format 85x55, lanscape card, square corners will be printed on thick high quality paper (300 or 350g)

Font styles to use
Sans Serif

Colors

Designer to choose colors to be used in the design.

Requirements
Must have
• Must be white, as the paper will be high quality, the paper will enhance the card.
• Name of the brand Halvard atelier (with specific font which make it very nice looking and catch the attention. similar to Calibri or Calibri
• Name of person (will give you the name later (4 names and position)
• the position of the person
• Mobile phone, e-mail, Physical address 27, rue Fenouillard, 75005 Paris, France (courrier only) our web site www.halvardatelier.fr
• The card must be simple and class
Nice to have
• Font of the address is smaller than the rest,
• Calibri font or similar on recto side with the name of the company which may look similar to the picture inserted in the brief.
• The grey color in the picture inserted is ok for us
Should not have
• Any parallel lines which represent the name of the company
• Any heavy design If you go on internet sites which present the furniture all designs are pure lines and high quality craftsmanship. To have an idea of our targetted client or brand we will be in touch: https://www.casavelumi.it/projects/
• Note that the picture added below is what we use, now as mail signature, up to you to have a better design etc.

```html
<!DOCTYPE html>
<html lang="fr">
<head>
<meta charset="utf-8">
<title>Halvard Atelier — Business Cards</title>
<link rel="stylesheet" href="https://fonts.googleapis.com/css2?family=Exo+2:wght@300;400&display=swap">
<style>
  :root {
    --backdrop: #e2e2e6;
    --paper: #ffffff;
    --gold: #c9a449;
    --ink-grey: #8e8e92;
    --ink-soft: #a4a4a8;
    --card-shadow: rgba(60, 62, 80, 0.16);
  }
  * { margin: 0; padding: 0; box-sizing: border-box; }
  html, body {
    width: 1200px;
    height: 756px;
    overflow: hidden;
    background: var(--backdrop);
    font-family: "Exo 2", sans-serif;
  }
  .cards {
    width: 1200px;
    height: 756px;
    display: flex;
    align-items: center;
    justify-content: center;
    gap: 40px;
  }
  .card {
    position: relative;
    width: 540px;
    height: 349px;
    background: var(--paper);
    box-shadow: 0 10px 28px var(--card-shadow);
  }
  /* Recto */
  .card--front {
    display: flex;
    align-items: center;
    justify-content: center;
  }
  .brand-name {
    font-weight: 300;
    font-size: 21px;
    letter-spacing: 6px;
    text-transform: uppercase;
    color: var(--gold);
    margin-left: 20px;
  }
  /* Verso */
  .holder {
    position: absolute;
    left: 160px;
    top: 112px;
    display: inline-flex;
    flex-direction: column;
    align-items: flex-end;
  }
  .holder__name {
    font-weight: 300;
    font-size: 21px;
    letter-spacing: 2.5px;
    color: var(--ink-grey);
  }
  .holder__role {
    font-weight: 300;
    font-size: 11px;
    letter-spacing: 3.5px;
    color: var(--ink-grey);
    margin-top: -2px;
  }
  .contact {
    position: absolute;
    left: 126px;
    top: 166px;
    list-style: none;
    font-weight: 300;
    font-size: 13px;
    line-height: 17px;
    color: var(--ink-grey);
  }
  .address {
    position: absolute;
    left: 96px;
    top: 290px;
    font-weight: 400;
    font-size: 7px;
    letter-spacing: 1.8px;
    color: var(--ink-soft);
  }
</style>
</head>
<body>
  <main class="cards">
    <section class="card card--back" aria-label="Verso de la carte">
      <div class="holder">
        <p class="holder__name">Élise Vaudrenne</p>
        <p class="holder__role">Assistant</p>
      </div>
      <ul class="contact">
        <li>+33 1 48 27 61 90</li>
        <li>www.elise.vaudrenne@lumenmail.fr</li>
        <li>www.halvardatelier.fr</li>
      </ul>
      <p class="address">27, rue Fenouillard, 75005 Paris, France</p>
    </section>
    <section class="card card--front" aria-label="Recto de la carte">
      <h1 class="brand-name">Halvard Atelier</h1>
    </section>
  </main>
</body>
</html>
```